Lanternfold Fellowship (LantFel) Corvale Institute of the Isles, Pelmont Ridge, Barbados

Seeking an informative and interactive website for the Lanternfold Fellowship on campus. The site is mainly to share with prospective students, their families and pastors/ churches what ministry the Society offers its members.

The Lanternfold Fellowship (LantFel) is an out reach ministry sponsored by the Southern Tidewater Circuit of Brightwell Assemblies, which is connected to the Brightwell Assembly of the Isles and Mainlands (BAIM) Connexion. The aim of the LanternfoldFellowship on the Pelmont Ridge campus is to mould social justice minded leaders for our region and beyond. Leaders who through their every day lives, seek to serve/ love God and their neighbours through three areas: Faith (spirituality), Mercy (hospitality) & Justice.

I am desiring originally, a six page website, with the option to expand.
Page 1: welcome/ introduction

Page 2: background/ history

Page3: Faith - explains the activities of theLanternfoldFellowship that seeks to build and strengthen the faith of its members and that of the campuses generally.

Page 4: Mercy - shares the hospitality offered by the Society to the campus and the students (assistance with settling in to a newish and,school, transportation, edicts assistance, grocery shopping assistance, student foster family programme etc)

Page 5: Justice- shares the social justice activities of the Lanternfold Fellowship such as the feeding programme for the homeless in the capital.

Page6: Let's Connect- contact page where students, pastors family members an email us or donate towards our various ministries and where the Societies memorabilia can be displayed and purchased

Target Market(s)

University students usually 18-30 years of age from across the Caribbean region

Industry/Entity Type

University

Number of Pages Required

5+ page

Requirements
Must have
• Ability to play videos and audio

```html
<!DOCTYPE html>
<html lang="en">
<head>
<meta charset="utf-8">
<title>Lanternfold Fellowship</title>
<link rel="stylesheet" href="https://fonts.googleapis.com/css2?family=Ubuntu:wght@300;400;500&display=swap">
<style>
:root{
  --cream:#f1f5dd;
  --green:#9bc423;
  --green-dark:#86ad14;
  --purple:#7b3f8e;
  --purple-dark:#5b2a6d;
  --text:#555a4a;
  --white:#ffffff;
}
*{box-sizing:border-box;margin:0;padding:0}
html,body{width:705px;height:1200px;overflow:hidden}
body{position:relative;background:var(--cream);font-family:"Ubuntu",sans-serif;color:var(--text)}
.abs{position:absolute}

.brand{left:0;width:705px;top:30px;display:flex;justify-content:center;align-items:center;gap:8px}
.brand-dot{width:22px;height:22px;border-radius:50%;background:var(--purple)}
.brand-name{font-size:17px;font-weight:500;color:var(--purple)}

.nav{left:66px;top:92px;width:574px;height:36px;background:var(--green);display:flex;align-items:center}
.nav a{color:var(--white);text-decoration:none;font-size:9px;padding:0 13px;height:36px;line-height:36px}
.nav a.active{background:var(--purple);width:56px;text-align:center;padding:0}
.nav .search{margin-left:10px;width:140px;height:18px;border-radius:9px;background:#a9cf3c;border:1px solid #b9d95e;display:flex;align-items:center;justify-content:space-between;padding:0 6px;font-size:6.5px;color:#eef6d8}

.hero{left:66px;top:128px;width:574px;height:244px;background:linear-gradient(180deg,#6d7580 0%,#a3a49c 45%,#c7ab78 72%,#2b2a24 86%,#151511 100%)}
.hero-title{left:408px;top:282px;font-size:17px;color:var(--white);font-weight:400}
.dots{left:340px;top:352px;display:flex;gap:4px}
.dots span{width:4px;height:4px;border-radius:50%;background:var(--white)}
.dots span.on{background:var(--purple)}

.welcome-title{left:0;width:705px;top:388px;text-align:center;color:var(--green);font-size:18px;font-weight:400}
.welcome-text{left:66px;width:574px;top:417px;text-align:center;font-size:7.4px;line-height:12px;font-weight:300;color:#4d5045}

.pillars{left:0;top:468px;width:705px;height:238px;background:var(--purple)}
.pillar{position:absolute;top:26px;width:181px}
.pillar .photo{width:181px;height:100px}
.pillar h3{font-size:8px;font-weight:400;color:var(--white);margin-top:13px}
.pillar p{font-size:6.3px;line-height:12px;color:#eadff0;font-weight:300;margin-top:7px}
.btn{display:inline-block;background:var(--green);color:var(--white);font-size:6.5px;padding:3px 9px;margin-top:10px;margin-left:-2px}

.sec-title{font-size:17px;color:var(--green);font-weight:400}
.chev{font-size:10px;color:var(--green)}
.rule{height:1px;background:#d6dac6}

.event-photo{left:66px;top:767px;width:148px;height:112px;background:linear-gradient(135deg,#e7e7de,#9b9a93 55%,#5b5650)}
.ribbon{left:74px;top:767px;width:32px;height:30px;background:var(--green);color:var(--white);font-size:6px;font-weight:500;text-align:center;line-height:7px;padding-top:7px}
.event-title{left:220px;top:765px;width:174px;font-size:8.5px;line-height:12px;color:var(--green)}
.event-text{left:220px;top:795px;width:174px;font-size:6.3px;line-height:12px;font-weight:300;color:#4d5045}
.btn-purple{left:220px;top:865px;background:var(--purple-dark);color:var(--white);font-size:6.5px;padding:4px 10px}

.news{left:408px;width:232px}
.news .date{position:absolute;left:0;top:0;width:42px;height:38px;background:var(--purple-dark);color:var(--white);font-size:6px;font-weight:500;text-align:center;line-height:8.5px;padding-top:6px}
.news h4{position:absolute;left:51px;top:0;font-size:8.5px;line-height:12px;font-weight:400;color:var(--purple-dark)}
.news p{position:absolute;left:51px;top:28px;font-size:6.3px;font-weight:300;color:#6a6d5f}

.testimonials{left:0;top:922px;width:705px;height:172px;background:var(--green)}
.test-title{left:0;width:705px;top:14px;text-align:center;color:var(--white);font-size:17px;font-weight:400}
.avatar{left:94px;top:50px;width:104px;height:104px;border-radius:50%;background:linear-gradient(180deg,#dfe3e6,#8e97a1 60%,#2e3440)}
.quote{left:202px;top:60px;font-size:12px;color:var(--white);font-weight:500}
.test-name{left:217px;top:75px;font-size:11px;color:var(--white);font-weight:500}
.test-text{left:217px;top:94px;width:400px;font-size:6.8px;line-height:12px;color:#f3f8e3;font-weight:300}
.arrow{top:83px;font-size:11px;color:var(--white)}

.social{top:1115px;width:22px;height:22px;border-radius:50%;border:1px solid var(--purple-dark)}
.social.alt{border-color:#2fa4d8}
.footer-links{left:0;width:705px;top:1152px;text-align:center;font-size:8px;color:#555}
.footer-links span{margin:0 6px;color:#777}
.copyright{left:0;width:705px;top:1174px;text-align:center;font-size:8px;color:#555}
</style>
</head>
<body>

<header class="abs brand">
  <span class="brand-dot"></span>
  <span class="brand-name">Lanternfold Fellowship</span>
</header>

<nav class="abs nav">
  <a class="active" href="#">Home</a>
  <a href="#">Welcome</a>
  <a href="#">Background</a>
  <a href="#">Faith</a>
  <a href="#">Mercy</a>
  <a href="#">Justice</a>
  <a href="#">Lets Connect</a>
  <div class="search"><span>Search</span>
    <svg width="7" height="7" viewBox="0 0 10 10"><circle cx="4" cy="4" r="3" fill="none" stroke="#fff" stroke-width="1.6"/><line x1="6.3" y1="6.3" x2="9" y2="9" stroke="#fff" stroke-width="1.6"/></svg>
  </div>
</nav>

<div class="abs hero" role="img" aria-label="Silhouette of a person with raised arms on a grassy hill under a dusk sky"></div>
<div class="abs hero-title">Lanternfold Fellowship</div>
<div class="abs dots"><span class="on"></span><span></span><span></span><span></span></div>

<h1 class="abs welcome-title">Welcome to Lanternfold Fellowship</h1>
<p class="abs welcome-text">The Lanternfold Fellowship (LantFel) is an out reach ministry sponsored by the Southern Tidewater Circuit of Brightwell Assemblies, which is connected to the Brightwell Assembly of the Isles and Mainlands (BAIM) Connexion. The aim of the LanternfoldFellowship on the Pelmont Ridge campus is to mould social justice minded leaders for our region and beyond.Leaders who through their every day lives, seek to serve/ love God and their neighbours</p>

<section class="abs pillars">
  <div class="pillar" style="left:66px">
    <div class="photo" role="img" aria-label="Silhouette of one person helping another up at sunset" style="background:linear-gradient(180deg,#5a2a12,#e07a1c 55%,#3a1a0a)"></div>
    <h3>Faith (spirituality)</h3>
    <p>Lorem Ipsum is simply dummy text of the printing and typesetting industry. Lorem Ipsum has been the industry's standard dummy text ever</p>
    <span class="btn">Read More</span>
  </div>
  <div class="pillar" style="left:262px">
    <div class="photo" role="img" aria-label="Black and white photo of hands folded in prayer" style="background:linear-gradient(135deg,#3a3a3a,#a8a8a8 50%,#555)"></div>
    <h3>Mercy (hospitality)</h3>
    <p>Lorem Ipsum is simply dummy text of the printing and typesetting industry. Lorem Ipsum has been the industry's standard dummy text ever</p>
    <span class="btn">Read More</span>
  </div>
  <div class="pillar" style="left:458px">
    <div class="photo" role="img" aria-label="Bronze scales of justice on a white background" style="background:linear-gradient(180deg,#f2f0ec,#b49a74 60%,#6b5230)"></div>
    <h3>Justice</h3>
    <p>Lorem Ipsum is simply dummy text of the printing and typesetting industry. Lorem Ipsum has been the industry's standard dummy text ever</p>
    <span class="btn">Read More</span>
  </div>
</section>

<h2 class="abs sec-title" style="left:65px;top:724px">Events</h2>
<div class="abs chev" style="left:382px;top:728px">&lsaquo; &rsaquo;</div>
<div class="abs rule" style="left:66px;top:752px;width:328px"></div>

<div class="abs event-photo" role="img" aria-label="Open hand reaching toward a bright sky"></div>
<div class="abs ribbon">APRIL<br>2015</div>
<div class="abs event-title">Lorem Ipsum is simply dummy text of the printing and typesetting industry.</div>
<p class="abs event-text">Lorem Ipsum is simply dummy text of the printing and typesetting industry. Lorem Ipsum has been the industry's standard dummy text ever since the 1500s, when an unknown printer took a galley of type and scrambled it to make a type specimen book.</p>
<span class="abs btn-purple">Read More</span>

<h2 class="abs sec-title" style="left:408px;top:724px">Latest News</h2>
<div class="abs chev" style="left:628px;top:728px">&lsaquo; &rsaquo;</div>
<div class="abs rule" style="left:408px;top:752px;width:232px"></div>

<article class="abs news" style="top:765px">
  <div class="date">25TH<br>APRIL<br>2015</div>
  <h4>Lorem Ipsum is simply dummy text of the printing and typesetting industry.</h4>
  <p>Lorem Ipsum has been the industry's standard</p>
</article>
<div class="abs rule" style="left:408px;top:818px;width:232px"></div>
<article class="abs news" style="top:835px">
  <div class="date">25TH<br>APRIL<br>2015</div>
  <h4>Lorem Ipsum is simply dummy text of the printing and typesetting industry.</h4>
  <p>Lorem Ipsum has been the industry's standard</p>
</article>

<section class="abs testimonials">
  <h2 class="abs test-title">Testimonials</h2>
  <div class="abs arrow" style="left:66px">&lsaquo;</div>
  <div class="abs avatar" role="img" aria-label="Portrait photo of a smiling man in a suit"></div>
  <div class="abs quote">&ldquo;</div>
  <div class="abs test-name">Dorian Wellsby</div>
  <p class="abs test-text">Lorem Ipsum is simply dummy text of the printing and typesetting industry. Lorem Ipsum has been the industry's standard dummy text ever since the 1500s, when an unknown printer took a galley of type and scrambled it to make a type specimen book. It has survived not only five centuries, but also the leap into electronic typesetting, remaining essentially unchanged.</p>
  <div class="abs arrow" style="left:634px">&rsaquo;</div>
</section>

<footer>
  <div class="abs social" style="left:327px"></div>
  <div class="abs social alt" style="left:356px"></div>
  <div class="abs footer-links">Home<span>|</span>Welcome<span>|</span>Background<span>|</span>Faith<span>|</span>Mercy<span>|</span>Justice<span>|</span>Lets Connect</div>
  <div class="abs copyright">&copy; 2015 Company Name .All Rights Reserved</div>
</footer>

</body>
</html>
```